Food truck menu design

Looking for a menu to be dissed for my toasted sandwich food truck. I have attached to logo and photo of the food truck for inspiration. if it can tie into them.
needing three sections, with titles:
CLASSICS
- classic one
. description
-Classic two
. Description
PREMIUM
- Premium one
. description
-Premium Two
. Description
-Premium Three
. Description
DESERT
-Desert one
. Description
-Desert two
.Description

also if it can be editable so I can change menu items and descriptions.

```html
<!DOCTYPE html>
<html lang="en">
<head>
<meta charset="UTF-8">
<title>Milo's Melts – Food Truck Menu</title>
<link href="https://fonts.googleapis.com/css2?family=Kanit:ital,wght@1,800&family=League+Spartan:wght@600&family=Cabin+Sketch:wght@700&family=Lora:ital@1&display=swap" rel="stylesheet">
<style>
  :root {
    --bg: #000000;
    --ink: #ffffff;
    --chalk: #f4efe6;
    --accent: #f7a21b;
    --cream: #fdf3d4;
    --faint: rgba(247, 162, 27, 0.07);
  }
  html, body { margin: 0; padding: 0; overflow: hidden; background: var(--bg); }
  .menu {
    position: relative;
    width: 1200px;
    height: 927px;
    overflow: hidden;
    background: var(--bg);
    color: var(--ink);
  }
  .backdrop-pattern {
    position: absolute; inset: 0;
    background: radial-gradient(circle at 50% 50%, #0a0806 0%, var(--bg) 70%);
  }
  .backdrop-mark {
    position: absolute;
    left: 327px; top: 254px;
    width: 480px; height: 480px;
    border-radius: 50%;
    background: var(--faint);
  }
  .brand {
    position: absolute;
    left: 34px; top: 128px;
    display: flex; align-items: center; gap: 14px;
  }
  .brand-dot {
    width: 56px; height: 56px; border-radius: 50%;
    background: var(--accent);
  }
  .brand-name {
    font-family: "League Spartan", sans-serif;
    font-weight: 600;
    font-size: 40px;
    color: var(--cream);
    margin: 0;
  }
  .headline {
    position: absolute;
    left: 300px; top: 212px;
    margin: 0;
    font-family: "Kanit", sans-serif;
    font-style: italic;
    font-weight: 800;
    font-size: 94px;
    line-height: 70px;
    color: var(--ink);
    transform: rotate(-19deg);
    transform-origin: 0 100%;
    white-space: nowrap;
    z-index: 2;
  }
  .headline span { display: block; }
  .headline .line-two { margin-left: -28px; }
  .section-title {
    position: absolute;
    margin: 0;
    font-family: "League Spartan", sans-serif;
    font-weight: 600;
    font-size: 44px;
    letter-spacing: 1px;
    color: var(--accent);
    line-height: 1;
  }
  .section-title.classics { left: 72px; top: 350px; z-index: 1; }
  .section-title.desert { left: 502px; top: 348px; }
  .section-title.premium { left: 892px; top: 177px; z-index: 3; }
  .item { position: absolute; }
  .item-row {
    display: flex; align-items: baseline; white-space: nowrap;
  }
  .item-name {
    font-family: "Cabin Sketch", sans-serif;
    font-weight: 700;
    font-size: 25px;
    color: var(--chalk);
  }
  .item-price {
    font-family: "League Spartan", sans-serif;
    font-weight: 600;
    font-size: 28px;
    color: var(--ink);
    margin-left: 4px;
  }
  .item-desc {
    margin: 14px 0 0;
    font-family: "Lora", serif;
    font-style: italic;
    font-size: 17px;
    line-height: 22px;
    text-align: center;
    color: var(--ink);
  }
  .col-classics { left: 29px; width: 350px; }
  .col-desert { left: 435px; width: 350px; }
  .col-premium { left: 829px; width: 350px; }
</style>
</head>
<body>
<main class="menu">
  <div class="backdrop-pattern" role="img" aria-label="Faint repeating pattern of toasted sandwich icons"></div>
  <div class="backdrop-mark" aria-hidden="true"></div>

  <div class="brand">
    <div class="brand-dot" aria-hidden="true"></div>
    <p class="brand-name">Milo's Melts</p>
  </div>

  <h1 class="headline"><span class="line-one">FOOD TRUCK</span><span class="line-two">FOOD MENU</span></h1>

  <h2 class="section-title classics">CLASSICS</h2>
  <h2 class="section-title desert">DESERT</h2>
  <h2 class="section-title premium">PREMIUM</h2>

  <div class="item col-classics" style="top:428px">
    <div class="item-row"><span class="item-name">Classic one...........</span><span class="item-price">$0.0</span></div>
    <p class="item-desc">description,description,description,-<br>descriptidescription,de-<br>scription,on,description,</p>
  </div>
  <div class="item col-classics" style="top:653px">
    <div class="item-row"><span class="item-name">Classic one...........</span><span class="item-price">$0.0</span></div>
    <p class="item-desc">description,description,description,-<br>descriptidescription,de-<br>scription,on,description,</p>
  </div>

  <div class="item col-desert" style="top:430px">
    <div class="item-row"><span class="item-name">Desert one............&nbsp;</span><span class="item-price">$0.0</span></div>
    <p class="item-desc">description,description,description,-<br>descriptidescription,de-<br>scription,on,description,</p>
  </div>
  <div class="item col-desert" style="top:635px">
    <div class="item-row"><span class="item-name">Desert two............&nbsp;</span><span class="item-price">$0.0</span></div>
    <p class="item-desc">description,description,description,-<br>descriptidescription,de-<br>scription,on,description,</p>
  </div>

  <div class="item col-premium" style="top:247px">
    <div class="item-row"><span class="item-name">Premium one........</span><span class="item-price">$0.0</span></div>
    <p class="item-desc">description,description,description,-<br>descriptidescription,de-<br>scription,on,description,</p>
  </div>
  <div class="item col-premium" style="top:437px">
    <div class="item-row"><span class="item-name">Premium two........&nbsp;</span><span class="item-price">$0.0</span></div>
    <p class="item-desc">description,description,description,-<br>descriptidescription,de-<br>scription,on,description,</p>
  </div>
  <div class="item col-premium" style="top:650px">
    <div class="item-row"><span class="item-name">Premium three.....</span><span class="item-price">$0.0</span></div>
    <p class="item-desc">description,description,description,-<br>descriptidescription,de-<br>scription,on,description,</p>
  </div>
</main>
</body>
</html>
```